Stylish new business card needed!

Hello everyone! I am in need of a new business card design for an alarm company here in Hurricane WV. I have all fonts, color codes and logos provided for you use! We are a young company and like the style of a clean sleek looking business card. Would like it double sided, one side holding the logo and the other with your design!
Target Market(s)
The people that are looking for the newest tech for home automation and security
Industry/Entity Type
Alarm services; Home automation
Contact Information for Business Card
Name of person; position (Sales; Installer); Phone Number (555.418.7290); Employee cell Number; Website (www.GuardedByVemlo.example); Employee Email; Double sided
Look and feel
Each slider illustrates characteristics of the customer's brand and the style your logo design should communicate.

```html
<!DOCTYPE html>
<html lang="en">
<head>
<meta charset="UTF-8">
<title>Vemlo Business Card</title>
<link rel="stylesheet" href="https://fonts.googleapis.com/css2?family=Montserrat:wght@400;500;700&display=swap">
<style>
  :root {
    --bg: #d3d6d6;
    --paper: #f7f7f5;
    --orange: #e8722e;
    --orange-card: #ee8745;
    --ink: #4a4a4a;
    --ink-soft: #666666;
    --emboss: #e6e4e0;
  }
  * { margin: 0; padding: 0; box-sizing: border-box; }
  html, body {
    width: 1200px; height: 829px; overflow: hidden;
    background: var(--bg);
    font-family: "Montserrat", Arial, sans-serif;
  }
  .sheet {
    width: 1200px; height: 829px;
    display: flex; align-items: center; justify-content: center; gap: 40px;
  }
  .card {
    width: 540px; height: 309px; position: relative;
    box-shadow: 0 10px 24px rgba(0,0,0,0.12);
  }
  .card--front { background: var(--paper); }
  .card--back {
    background: var(--orange-card);
    display: flex; align-items: center; justify-content: center;
  }

  .person { position: absolute; top: 30px; left: 0; padding-left: 34px; }
  .person__marker {
    position: absolute; left: 0; top: 2px;
    width: 14px; height: 24px; background: var(--orange);
  }
  .person__name {
    color: var(--orange); font-weight: 700; font-size: 17px; letter-spacing: 1.2px;
    text-transform: uppercase; line-height: 1.1;
  }
  .person__role { color: var(--ink-soft); font-size: 11px; margin-top: 2px; }

  .contacts { position: absolute; left: 34px; top: 140px; list-style: none; }
  .contacts li {
    display: flex; align-items: center; gap: 8px;
    font-size: 11.5px; color: var(--ink); margin-bottom: 9px;
  }
  .contacts svg { width: 11px; height: 11px; flex: none; }

  .wordmark {
    font-weight: 500; letter-spacing: 3px; line-height: 1;
    display: flex; align-items: center; gap: 10px;
  }
  .wordmark__dot { width: 12px; height: 12px; border-radius: 50%; background: var(--orange); }
  .card--front .wordmark {
    position: absolute; right: 40px; top: 108px;
    font-size: 54px; color: var(--ink);
  }
  .card--back .wordmark { font-size: 96px; color: var(--emboss); }

  .address {
    position: absolute; right: 34px; bottom: 28px;
    text-align: right; font-size: 11.5px; color: var(--ink); line-height: 1.5;
    font-style: normal;
  }
</style>
</head>
<body>
<main class="sheet">
  <section class="card card--front" aria-label="Business card front">
    <header class="person">
      <span class="person__marker"></span>
      <h1 class="person__name">Daria Kellen</h1>
      <p class="person__role">Sales/Installer</p>
    </header>

    <ul class="contacts">
      <li>
        <svg viewBox="0 0 12 12" aria-hidden="true"><path d="M3 1 L5 3.5 L4 5 Q5 7 7 8 L8.5 7 L11 9 L9.5 11 Q5 11 2.5 8 Q0.5 5 1 2.5 Z" fill="var(--orange)"/></svg>
        555.418.7290
      </li>
      <li>
        <svg viewBox="0 0 12 12" aria-hidden="true"><rect x="0.5" y="2.5" width="11" height="7" fill="var(--orange)"/><path d="M0.5 2.5 L6 7 L11.5 2.5" fill="none" stroke="var(--paper)" stroke-width="1"/></svg>
        info@GuardedByVemlo.example
      </li>
      <li>
        <svg viewBox="0 0 12 12" aria-hidden="true"><circle cx="6" cy="6" r="5" fill="none" stroke="var(--orange)" stroke-width="1.2"/><ellipse cx="6" cy="6" rx="2.2" ry="5" fill="none" stroke="var(--orange)" stroke-width="1"/><line x1="1" y1="6" x2="11" y2="6" stroke="var(--orange)" stroke-width="1"/></svg>
        www.GuardedByVemlo.example
      </li>
    </ul>

    <div class="wordmark"><span class="wordmark__dot"></span>VEMLO</div>

    <address class="address">
      418 W Harlow Avenue<br>
      Bramble County Name 6072
    </address>
  </section>

  <section class="card card--back" aria-label="Business card back">
    <div class="wordmark">VEMLO</div>
  </section>
</main>
</body>
</html>
```